Flyer Design for Earthworks Business in Australia

Gully Crest Earthworks is a new Earthworks and mini excavator business in Australia that requires an attention grabbing flyer to be used in our promotional material.

It will be dual sided and will be used for print media and also digital marketing. It will incorporate our logo, contact details and a list of our services offered.

Target Market(s)

Prospective clients that require earthworks

Industry/Entity Type

Construction and Earthworks

Requirements
Must have
• Must be dual sided, include our logo and contact information (phone number and Web page) and our services offered.
Nice to have
• QR link for Web site. Some photo(s) incorporated into the design.

```html
<!DOCTYPE html>
<html lang="en">
<head>
<meta charset="utf-8">
<title>Gully Crest Earthworks – Flyer</title>
<link href="https://fonts.googleapis.com/css2?family=Poppins:wght@400;500;600;700;800&display=swap" rel="stylesheet">
<style>
:root{
  --lime:#c6dc2b;
  --black:#0c0c0c;
  --charcoal:#3a3a3a;
  --grey:#2b2b2b;
  --white:#ffffff;
  --paper:#ffffff;
}
*{margin:0;padding:0;box-sizing:border-box}
html,body{width:1200px;height:1200px;overflow:hidden;background:var(--paper)}
body{position:relative;font-family:'Poppins',sans-serif;color:var(--white)}
.page{position:absolute;top:233px;width:524px;height:741px;overflow:hidden;background:var(--black)}
.page--front{left:69px}
.page--back{left:615px}
.shapes{position:absolute;inset:0;width:524px;height:741px}
.abs{position:absolute}
.photo{position:absolute}
.headline{left:37px;top:36px;font-weight:700;font-size:21px;line-height:28px;color:var(--lime)}
.brand{position:absolute;text-align:center;color:var(--white);font-weight:700;letter-spacing:1px}
.brand__mark{display:block;margin:0 auto 8px;width:26px;height:26px;background:var(--lime)}
.brand__name{display:block;line-height:1.15}
.front-brand{left:300px;top:70px;width:200px;font-size:20px}
.back-brand{left:330px;top:22px;width:136px;font-size:13px}
.back-brand .brand__mark{width:20px;height:20px;margin-bottom:6px}
.intro{font-size:10.4px;color:var(--black);white-space:nowrap;line-height:14px}
.intro b{font-weight:700}
.committed-title{left:0;width:524px;top:470px;text-align:center;font-weight:600;font-size:15px}
.pledge{position:absolute;top:499px;width:107px;height:105px;border:1px solid var(--lime);text-align:center}
.pledge__icon{display:block;margin:10px auto 4px;width:36px;height:36px}
.pledge__text{font-weight:700;font-size:10.4px;line-height:13px}
.tagline{left:0;width:524px;top:616px;text-align:center;font-size:14px;color:var(--lime)}
.contact{left:34px;font-size:11px;line-height:16px;display:flex;align-items:center;gap:6px}
.contact svg{width:9px;height:10px}
.contact--pin{color:var(--lime);font-weight:600}
.cta-label{left:306px;top:659px;font-size:18px;font-weight:500;color:var(--black);line-height:22px}
.cta-number{left:306px;top:679px;font-size:22.5px;font-weight:800;color:var(--black);line-height:28px;letter-spacing:.3px}
.section-title{left:72px;top:46px;font-size:19px;font-weight:700;color:var(--black)}
.service__title{position:absolute;font-size:14px;font-weight:700;color:var(--lime);line-height:16.5px}
.service__icon{position:absolute;width:34px;height:34px;border-radius:50%;background:var(--lime);border:2px solid var(--white)}
.service__list{position:absolute;list-style:none;font-size:10px;line-height:14px}
.service__list li{position:relative;padding-left:7px}
.service__list li::before{content:"›";position:absolute;left:0;top:-1px;color:var(--lime);font-weight:700}
</style>
</head>
<body>

<!-- FRONT -->
<section class="page page--front">
  <svg class="shapes" viewBox="0 0 524 741" aria-hidden="true">
    <polygon points="372,0 524,0 524,179 200,179" fill="var(--charcoal)"/>
  </svg>
  <div class="photo" role="img" aria-label="Photo of a yellow mini excavator parked on a grassy field under a blue sky" style="left:0;top:179px;width:524px;height:275px;background:linear-gradient(180deg,#86aed6 0%,#c9dbec 32%,#5f6b35 55%,#8b8a52 100%)"></div>
  <div class="photo" role="img" aria-label="Darkened photo of a work truck carrying a mini excavator" style="left:0;top:454px;width:524px;height:213px;background:linear-gradient(180deg,#3b3c37 0%,#2c2d2a 100%)"></div>
  <svg class="shapes" viewBox="0 0 524 741" aria-hidden="true">
    <polygon points="500,179 524,179 524,454 106,454 225,357 431,357 362,304" fill="var(--lime)"/>
    <polygon points="0,398 28,398 56,426 28,454 0,454 28,426" fill="var(--white)"/>
    <polygon points="0,398 0,398" fill="none"/>
    <polygon points="52,398 80,398 108,426 80,454 52,454 80,426" fill="var(--white)"/>
    <polygon points="0,410 16,426 0,442" fill="var(--black)"/>
    <polygon points="25,484 42,484 56,499 42,514 25,514 39,499" fill="var(--lime)"/>
    <polygon points="505,544 488,544 474,559 488,573 505,573 491,559" fill="var(--lime)"/>
    <rect x="0" y="667" width="524" height="74" fill="var(--charcoal)"/>
    <polygon points="330,718 524,718 524,741 310,741" fill="var(--black)"/>
    <polygon points="212,650 438,650 511,718 284,718" fill="var(--lime)"/>
    <line x1="470" y1="687" x2="524" y2="687" stroke="var(--lime)" stroke-width="1"/>
    <line x1="410" y1="718" x2="385" y2="741" stroke="var(--lime)" stroke-width="1"/>
    <circle cx="278" cy="673" r="16" fill="var(--black)"/>
    <path d="M271 666c1-2 3-2 4 0l2 3c1 1 0 2-1 3 1 2 3 4 5 5 1-1 2-2 3-1l3 2c2 1 2 3 0 4-3 3-9 0-13-4s-6-9-3-12z" fill="none" stroke="var(--lime)" stroke-width="1.6"/>
  </svg>

  <h1 class="abs headline">Precision Earthworks.<br>Solid Foundations.<br>Built to Last.</h1>
  <div class="brand front-brand"><span class="brand__mark"></span><span class="brand__name">GULLY CREST<br>EARTHWORKS</span></div>

  <p class="abs intro" style="left:228px;top:367px">Gully Crest Earthworks is your <b>Perth</b></p>
  <p class="abs intro" style="left:213px;top:382px">based mini excavator and earthworks</p>
  <p class="abs intro" style="left:197px;top:396px">business delivering precise, efficient, and</p>
  <p class="abs intro" style="left:181px;top:411px">dependable excavation services for</p>
  <p class="abs intro" style="left:165px;top:427px">residential and small commercial projects.</p>

  <h2 class="abs committed-title">WE ARE COMMITTED TO</h2>
  <div class="pledge" style="left:40px">
    <svg class="pledge__icon" viewBox="0 0 36 36" fill="none" stroke="var(--lime)" stroke-width="1.6"><path d="M8 33V20h6l4-9c2 0 3 2 2 5h7c2 0 2 3 0 3 2 0 2 3 0 3 2 0 2 3 0 3l-1 8H8z"/><path d="M10 4l1.5 3 3 .5-2 2 .5 3-3-1.5-3 1.5.5-3-2-2 3-.5z"/></svg>
    <p class="pledge__text">Delivering<br>high-quality<br>workmanship</p>
  </div>
  <div class="pledge" style="left:152px">
    <svg class="pledge__icon" viewBox="0 0 36 36" fill="none" stroke="var(--lime)" stroke-width="1.6"><rect x="4" y="3" width="24" height="18" rx="2"/><path d="M16 7v10M19 9h-4a2 2 0 000 3h2a2 2 0 010 3h-4"/><path d="M10 21l-2 6 6-6M20 26h12v7H20z"/></svg>
    <p class="pledge__text">Maintainin<br>clear and honest<br>communication</p>
  </div>
  <div class="pledge" style="left:264px">
    <svg class="pledge__icon" viewBox="0 0 36 36" fill="none" stroke="var(--lime)" stroke-width="1.6"><circle cx="18" cy="18" r="12"/><circle cx="18" cy="18" r="5"/><path d="M18 2v4M18 30v4M2 18h4M30 18h4M7 7l3 3M26 26l3 3M29 7l-3 3M7 29l3-3"/></svg>
    <p class="pledge__text">Completing<br>projects safely<br>and efficiently</p>
  </div>
  <div class="pledge" style="left:376px">
    <svg class="pledge__icon" viewBox="0 0 36 36" fill="none" stroke="var(--lime)" stroke-width="1.6"><path d="M12 3l6 9 6-9"/><circle cx="18" cy="22" r="10"/><path d="M18 16l2 4 4 .5-3 3 1 4-4-2-4 2 1-4-3-3 4-.5z"/></svg>
    <p class="pledge__text">Providing<br>reliable service<br>you can count on</p>
  </div>
  <p class="abs tagline">Strong Foundations. Reliable Service. Quality Results.</p>

  <p class="abs contact contact--pin" style="top:673px"><svg viewBox="0 0 9 10"><path d="M4.5 10S1 6 1 3.5a3.5 3.5 0 017 0C8 6 4.5 10 4.5 10z" fill="var(--lime)"/></svg>Ridgeford, Western Australia</p>
  <p class="abs contact" style="top:690px"><svg viewBox="0 0 9 10"><rect x=".5" y="2" width="8" height="6" fill="var(--white)"/><path d="M.5 2l4 3 4-3" stroke="var(--charcoal)" fill="none"/></svg>admin@gullycrest.com.au</p>
  <p class="abs contact" style="top:706px"><svg viewBox="0 0 9 10"><circle cx="4.5" cy="5" r="4" fill="none" stroke="var(--white)"/><path d="M.5 5h8M4.5 1v8" stroke="var(--white)"/></svg>www.gullycrest.com.au</p>
  <p class="abs cta-label">CALL US 24/7</p>
  <p class="abs cta-number">0455 218 306</p>
</section>

<!-- BACK -->
<section class="page page--back">
  <svg class="shapes" viewBox="0 0 524 741" aria-hidden="true">
    <polygon points="288,91 524,91 524,310" fill="var(--charcoal)"/>
    <polygon points="0,0 191,0 288,91 79,91 79,220 0,220" fill="var(--lime)"/>
    <polygon points="0,17 72,91 0,91" fill="var(--black)"/>
    <polygon points="0,160 79,92 0,92" fill="var(--black)"/>
    <polygon points="341,472 491,472 524,501 524,642 341,642" fill="var(--lime)"/>
    <polygon points="0,540 75,640 119,667 0,667" fill="var(--lime)"/>
    <polygon points="0,459 28,459 56,487 28,516 0,516 20,487" fill="var(--white)"/>
    <polygon points="52,459 80,459 108,487 80,516 52,516 72,487" fill="var(--white)"/>
    <polygon points="0,477 6,487 0,497" fill="var(--black)"/>
    <rect x="0" y="667" width="524" height="74" fill="var(--charcoal)"/>
    <polygon points="330,718 524,718 524,741 310,741" fill="var(--black)"/>
    <polygon points="212,650 438,650 511,718 284,718" fill="var(--lime)"/>
    <line x1="470" y1="687" x2="524" y2="687" stroke="var(--lime)" stroke-width="1"/>
    <line x1="410" y1="718" x2="385" y2="741" stroke="var(--lime)" stroke-width="1"/>
    <circle cx="278" cy="673" r="16" fill="var(--black)"/>
    <path d="M271 666c1-2 3-2 4 0l2 3c1 1 0 2-1 3 1 2 3 4 5 5 1-1 2-2 3-1l3 2c2 1 2 3 0 4-3 3-9 0-13-4s-6-9-3-12z" fill="none" stroke="var(--lime)" stroke-width="1.6"/>
  </svg>

  <h2 class="abs section-title">OUR SERVICES</h2>
  <div class="brand back-brand"><span class="brand__mark"></span><span class="brand__name">GULLY CREST<br>EARTHWORKS</span></div>

  <span class="service__icon" style="left:110px;top:105px"></span>
  <h3 class="service__title" style="left:150px;top:106px">Excavation &amp;<br>site preparation</h3>
  <ul class="service__list" style="left:107px;top:145px"><li>Site clearing and levelling</li><li>Bulk earthworks</li><li>Land reshaping and grading</li><li>Soil removal and preparation</li></ul>

  <span class="service__icon" style="left:301px;top:105px"></span>
  <h3 class="service__title" style="left:341px;top:114px">Trenching</h3>
  <ul class="service__list" style="left:298px;top:145px"><li>Electrical and communication lines</li><li>Water and sewer pipes</li><li>Irrigation systems</li><li>Foundation trenches</li></ul>

  <span class="service__icon" style="left:110px;top:215px"></span>
  <h3 class="service__title" style="left:150px;top:218px">Pad &amp; slab<br>preparation</h3>
  <ul class="service__list" style="left:107px;top:257px"><li>House pads</li><li>Shed slabs</li><li>Garage foundations</li><li>Commercial slab preparation</li></ul>

  <span class="service__icon" style="left:301px;top:215px"></span>
  <h3 class="service__title" style="left:341px;top:218px">Drainage &amp;<br>earthmoving support</h3>
  <ul class="service__list" style="left:298px;top:257px"><li>Stormwater drainage systems</li><li>Surface water management</li><li>Earthmoving for landscaping and<br>site correction</li><li>Backfilling and compaction</li></ul>

  <span class="service__icon" style="left:110px;top:342px"></span>
  <h3 class="service__title" style="left:150px;top:344px">Footing &amp;<br>foundations</h3>
  <ul class="service__list" style="left:107px;top:384px"><li>Strip footings</li><li>Pier foundations</li><li>Reinforced footing preparation</li><li>Accurate depth and alignment</li></ul>

  <span class="service__icon" style="left:301px;top:342px"></span>
  <h3 class="service__title" style="left:341px;top:344px">Machine hire<br>with operator</h3>
  <ul class="service__list" style="left:298px;top:384px"><li>Short-term or long-term hire</li><li>Residential and commercial<br>projects</li><li>Earthmoving and excavation<br>support</li></ul>

  <div class="photo" role="img" aria-label="Photo of a mini excavator beside a freshly dug trench on a grassy block" style="left:47px;top:487px;width:137px;height:149px;background:linear-gradient(180deg,#8db4dc 0%,#bfd4e8 35%,#6e7a44 60%,#8c6d4a 100%)"></div>
  <div class="photo" role="img" aria-label="Photo of a white tipper truck carrying a mini excavator on a dirt lot" style="left:194px;top:487px;width:137px;height:149px;background:linear-gradient(180deg,#4f6a3a 0%,#7a8c5a 40%,#d9d6cc 60%,#b79d74 100%)"></div>
  <div class="photo" role="img" aria-label="Photo of a long trench dug across a grassy paddock" style="left:339px;top:487px;width:137px;height:149px;background:linear-gradient(180deg,#7fa9d6 0%,#c5d8ea 30%,#667b3e 55%,#8c6a48 100%)"></div>

  <p class="abs contact contact--pin" style="top:673px"><svg viewBox="0 0 9 10"><path d="M4.5 10S1 6 1 3.5a3.5 3.5 0 017 0C8 6 4.5 10 4.5 10z" fill="var(--lime)"/></svg>Ridgeford, Western Australia</p>
  <p class="abs contact" style="top:690px"><svg viewBox="0 0 9 10"><rect x=".5" y="2" width="8" height="6" fill="var(--white)"/><path d="M.5 2l4 3 4-3" stroke="var(--charcoal)" fill="none"/></svg>admin@gullycrest.com.au</p>
  <p class="abs contact" style="top:706px"><svg viewBox="0 0 9 10"><circle cx="4.5" cy="5" r="4" fill="none" stroke="var(--white)"/><path d="M.5 5h8M4.5 1v8" stroke="var(--white)"/></svg>www.gullycrest.com.au</p>
  <p class="abs cta-label">CALL US 24/7</p>
  <p class="abs cta-number">0455 218 306</p>
</section>

</body>
</html>
```